Radio Service company needs ad for trade publication

Airwave Partners provides sales, content, production, technology, and promotion products and services to radio stations to help increase sales and solutions to improve operations and reduce costs. We are looking for a creative ad (sizes 720x250, 300x250, 728x180) with a theme around "MASTER YOUR 2024 BUDGET with AIRWAVE PARTNERS". Categories we have products/services to help them get budget into alignment. (1) Sales (2) Content & Programming (3) Technology (4) Production & Imaging (5) Promotions & Marketing (6) Support Services
"Don't go into the new year with an Unrealistic Budget.....We can Help!"

```html
<!DOCTYPE html>
<html lang="en">
<head>
<meta charset="utf-8">
<title>Airwave Partners – Master Your 2024 Budget ad set</title>
<link rel="stylesheet" href="https://fonts.googleapis.com/css2?family=Archivo:wght@300;600;700;800&display=swap">
<style>
  :root {
    --page: #e3e3e3;
    --white: #ffffff;
    --navy: #2a3e8f;
    --blue: #3a6fc0;
    --sky: #4a93d2;
    --photo-light: #a7b1d0;
    --photo-dark: #2b3358;
  }
  * { box-sizing: border-box; margin: 0; padding: 0; }
  html, body { width: 851px; height: 1200px; overflow: hidden; background: var(--page); }
  body { font-family: "Archivo", "Helvetica Neue", Arial, sans-serif; }

  .sheet { position: absolute; left: 0; top: 0; width: 881px; height: 1242px; transform: scale(0.9659); transform-origin: 0 0; }

  .banner { position: absolute; background: var(--white); overflow: hidden; }
  .banner svg.art { position: absolute; left: 0; top: 0; }

  .headline { position: absolute; color: var(--navy); font-weight: 800; text-transform: uppercase; white-space: nowrap; }
  .with { position: absolute; color: var(--blue); font-weight: 300; }
  .brand { position: absolute; color: var(--sky); font-weight: 700; text-transform: uppercase; line-height: 0.98; letter-spacing: -0.5px; white-space: nowrap; }

  .cta {
    position: absolute; display: flex; align-items: center; justify-content: center;
    border-radius: 999px; color: var(--white); font-weight: 700; text-transform: uppercase;
    background: linear-gradient(90deg, var(--sky), var(--navy));
  }
  .cta--solid { background: var(--navy); }

  .tagline-band { position: absolute; color: var(--white); font-weight: 600; background: linear-gradient(90deg, var(--navy), var(--sky)); }

  /* Leaderboard 720 x 250 */
  .banner--wide { left: 68px; top: 62px; width: 720px; height: 249px; }
  .banner--wide .headline { left: 405px; top: 17px; font-size: 28px; line-height: 34px; }
  .banner--wide .with { left: 447px; top: 84px; font-size: 29px; }
  .banner--wide .brand { left: 519px; top: 95px; font-size: 33px; }
  .banner--wide .cta { left: 522px; top: 166px; width: 166px; height: 32px; font-size: 12px; }
  .banner--wide .tagline-band { left: 0; top: 219px; width: 720px; height: 30px; font-size: 14.5px; display: flex; align-items: center; justify-content: center; }

  /* Strip 728 x 120 */
  .banner--strip { left: 68px; top: 367px; width: 728px; height: 120px; }
  .banner--strip .headline { left: 216px; top: 12px; font-size: 19px; line-height: 23px; }
  .banner--strip .with { left: 243px; top: 58px; font-size: 20px; }
  .banner--strip .brand { left: 290px; top: 63px; font-size: 21px; }
  .banner--strip .panel-copy { position: absolute; left: 458px; top: 16px; width: 260px; color: var(--white); font-weight: 600; font-size: 13.4px; line-height: 17.5px; }
  .banner--strip .cta { left: 458px; top: 80px; width: 122px; height: 23px; font-size: 9.5px; }

  /* Medium rectangle 300 x 250 */
  .banner--square { left: 68px; top: 572px; width: 300px; height: 250px; }
  .banner--square .headline { left: 98px; top: 16px; font-size: 18.5px; line-height: 23px; }
  .banner--square .with { left: 127px; top: 62px; font-size: 19px; }
  .banner--square .brand { left: 170px; top: 68px; font-size: 21px; }
  .banner--square .cta { left: 168px; top: 121px; width: 122px; height: 25px; font-size: 9.5px; }
  .banner--square .tagline-band { left: 0; top: 182px; width: 300px; height: 68px; font-size: 13.6px; line-height: 19px; text-align: center; padding-top: 8px; }

  /* Skyscraper 160 x 600 */
  .banner--tower { left: 636px; top: 572px; width: 160px; height: 600px; }
  .banner--tower .headline { left: 17px; top: 22px; font-size: 25px; line-height: 32.5px; }
  .banner--tower .with { left: 18px; top: 151px; font-size: 20px; }
  .banner--tower .brand { left: 17px; top: 182px; font-size: 21px; }
  .banner--tower .cta { left: 18px; top: 253px; width: 122px; height: 24px; font-size: 9.5px; }
  .banner--tower .tagline-band { left: 0; top: 298px; width: 160px; height: 302px; padding: 12px 18px 0 17px; font-size: 13.6px; line-height: 18.2px; background: linear-gradient(180deg, var(--sky), var(--navy)); }
</style>
</head>
<body>
<main class="sheet">

  <section class="banner banner--wide" aria-label="Airwave Partners 720 by 250 ad">
    <svg class="art" width="720" height="219" viewBox="0 0 720 219">
      <defs>
        <linearGradient id="photoWide" x1="0" y1="0" x2="1" y2="1">
          <stop offset="0" stop-color="var(--photo-light)"/>
          <stop offset="1" stop-color="var(--photo-dark)"/>
        </linearGradient>
      </defs>
      <path class="accent-arc" d="M0,0 H150 Q320,60 430,219 H0 Z" fill="var(--sky)"/>
      <circle role="img" aria-label="Studio microphone with pop filter over a mixing desk" cx="230" cy="300" r="262" fill="url(#photoWide)"/>
    </svg>
    <h1 class="headline">Master your<br>2024 budget</h1>
    <span class="with">with</span>
    <span class="brand">Airwave<br>Partners</span>
    <a class="cta">Get started now</a>
    <p class="tagline-band">Unlock budget harmony for your radio station. Tailored solutions in sales, content, tech, and more.</p>
  </section>

  <section class="banner banner--strip" aria-label="Airwave Partners 728 by 120 ad">
    <svg class="art" width="728" height="120" viewBox="0 0 728 120">
      <defs>
        <linearGradient id="photoStrip" x1="0" y1="0" x2="1" y2="1">
          <stop offset="0" stop-color="var(--photo-light)"/>
          <stop offset="1" stop-color="var(--photo-dark)"/>
        </linearGradient>
        <linearGradient id="panelStrip" x1="0" y1="0" x2="1" y2="0">
          <stop offset="0" stop-color="var(--sky)"/>
          <stop offset="1" stop-color="var(--navy)"/>
        </linearGradient>
      </defs>
      <path class="accent-arc" d="M0,8 Q50,4 85,30 L60,120 H0 Z" fill="var(--sky)"/>
      <circle role="img" aria-label="Studio microphone with pop filter over a mixing desk" cx="110" cy="150" r="124" fill="url(#photoStrip)"/>
      <path class="copy-panel" d="M436,0 Q418,60 444,120 H728 V0 Z" fill="url(#panelStrip)"/>
    </svg>
    <h2 class="headline">Master your<br>2024 budget</h2>
    <span class="with">with</span>
    <span class="brand">Airwave<br>Partners</span>
    <p class="panel-copy">Unlock budget harmony for your radio station. Tailored solutions in sales, content, tech, and more.</p>
    <a class="cta cta--solid">Get started now</a>
  </section>

  <section class="banner banner--square" aria-label="Airwave Partners 300 by 250 ad">
    <svg class="art" width="300" height="182" viewBox="0 0 300 182">
      <defs>
        <linearGradient id="photoSquare" x1="0" y1="0" x2="1" y2="1">
          <stop offset="0" stop-color="var(--photo-light)"/>
          <stop offset="1" stop-color="var(--photo-dark)"/>
        </linearGradient>
      </defs>
      <path class="accent-arc" d="M0,0 H30 Q55,15 72,38 L40,182 H0 Z" fill="var(--sky)"/>
      <path role="img" aria-label="Studio microphone with pop filter over a mixing desk" d="M0,38 Q55,22 95,68 Q135,112 160,182 H0 Z" fill="url(#photoSquare)"/>
    </svg>
    <h2 class="headline">Master your<br>2024 budget</h2>
    <span class="with">with</span>
    <span class="brand">Airwave<br>Partners</span>
    <a class="cta">Get started now</a>
    <p class="tagline-band">Unlock budget harmony for your<br>radio station. Tailored solutions in<br>sales, content, tech, and more.</p>
  </section>

  <section class="banner banner--tower" aria-label="Airwave Partners 160 by 600 ad">
    <h2 class="headline">Master<br>your<br>2024<br>budget</h2>
    <span class="with">with</span>
    <span class="brand">Airwave<br>Partners</span>
    <a class="cta">Get started now</a>
    <p class="tagline-band">Unlock budget harmony for your radio station. Tailored solutions in sales, content, tech, and more.</p>
    <svg class="art" width="160" height="600" viewBox="0 0 160 600">
      <defs>
        <linearGradient id="photoTower" x1="0" y1="0" x2="1" y2="1">
          <stop offset="0" stop-color="var(--photo-light)"/>
          <stop offset="1" stop-color="var(--photo-dark)"/>
        </linearGradient>
      </defs>
      <path class="white-arc" d="M0,450 Q85,410 160,535 V600 H0 Z" fill="var(--white)"/>
      <path role="img" aria-label="Studio microphone with pop filter over a mixing desk" d="M0,458 Q75,428 125,490 Q152,530 160,600 H0 Z" fill="url(#photoTower)"/>
    </svg>
  </section>

</main>
</body>
</html>
```